MossVane Spa, Skincare and Cosmetics website

I need a website for MossVane (putting the glow back into people's skin) which allows viewers to access information about Beauty Spa packaging and facilities as well as online skincare and cosmetic products. Our distinctive difference is that our products are certified organic. We want to target a luxury high income niche market (age 30-50). I want all colours to be "baby colours" preferably background to be "baby metallic pink" (but please don't make the website too immature) with curves as patterns. I want a romantic vintage look.

The website needs to look:
1. elegant (prestige and luxury)
2. bright (baby colours mainly)
3. European curves and signature patterns
4. Can include Pearl related pics (but not a must)

The website pages needs to have:
1. pages ordering skincare/cosmetics
2. shopping cart and payment
3. about us and about our product differences
4. contact us
5. booking for spa treatments and packages

I have attached our logo and also packaging label styles.

Industry/Entity Type

Cosmetics

```html
<!DOCTYPE html>
<html lang="en">
<head>
<meta charset="utf-8">
<title>MossVane Spa, Skincare and Cosmetics</title>
<link rel="stylesheet" href="https://fonts.googleapis.com/css2?family=PT+Sans:ital,wght@0,400;0,700;1,400&display=swap">
<style>
  :root {
    --canvas-grey: #efefef;
    --white: #ffffff;
    --ink: #444444;
    --ink-soft: #666666;
    --charcoal: #222222;
    --charcoal-panel: #252525;
    --rose: #b99c8f;
    --rose-light: #d6b5a8;
    --rose-pale: #e8d5cc;
    --blush: #f1ddd6;
    --rule: #dddddd;
  }
  * { box-sizing: border-box; margin: 0; padding: 0; }
  html, body {
    width: 1200px; height: 1000px; overflow: hidden;
    background: var(--white);
    font-family: "PT Sans", Arial, sans-serif;
    color: var(--ink);
  }
  .page { position: relative; width: 1200px; height: 1000px; overflow: hidden; }
  .abs { position: absolute; }

  /* Hero */
  .hero { left: 0; top: 0; width: 1200px; height: 320px; background: var(--canvas-grey); }
  .hero-photo {
    left: 540px; top: 0; width: 400px; height: 310px;
    background: radial-gradient(ellipse at 65% 35%, #3a3a3a 0%, #6e6e6e 35%, #d8d8d8 70%, var(--canvas-grey) 100%);
  }
  .brand { display: flex; align-items: center; gap: 8px; color: var(--rose); }
  .brand-dot { width: 22px; height: 22px; border-radius: 50%; background: var(--rose); }
  .brand-name { font-size: 19px; letter-spacing: 1px; }
  .hero-brand { left: 266px; top: 140px; }
  .hero-title { left: 265px; top: 173px; font-size: 28px; color: var(--rose); letter-spacing: 0.3px; }
  .hero-lead { left: 266px; top: 230px; width: 270px; font-size: 14.5px; line-height: 17px; color: var(--ink-soft); }
  .slide-btn {
    top: 276px; width: 29px; height: 24px; background: var(--rose-light);
    display: flex; align-items: center; justify-content: center;
  }
  .slide-prev { left: 579px; }
  .slide-next { left: 613px; }
  .social { top: 282px; width: 19px; height: 19px; background: #2a2a2a; }
  .social-plus { display: flex; align-items: center; justify-content: center; }

  /* Utility bar */
  .util-link { top: 2px; font-size: 8px; color: var(--rose); }
  .util-tab {
    left: 776px; top: 0; width: 80px; height: 14px; background: var(--rose-pale);
    clip-path: polygon(0 0, 100% 0, 88% 100%, 10% 100%);
  }
  .cart { left: 858px; top: 2px; font-size: 8px; color: var(--ink-soft); }
  .cart-icon { left: 922px; top: 1px; }

  /* Navigation */
  .nav-band { left: 0; top: 320px; width: 1200px; height: 94px; background: var(--charcoal); }
  .nav-panel { left: 266px; top: 309px; width: 671px; height: 105px; background: var(--charcoal-panel); border-radius: 6px 6px 0 0; }
  .nav-brand { left: 285px; top: 347px; color: #d9c0b5; }
  .nav-brand .brand-dot { background: #d9c0b5; width: 26px; height: 26px; }
  .nav-item { top: 353px; font-size: 8.5px; color: var(--white); text-transform: uppercase; letter-spacing: 0.2px; }
  .nav-active-bar { left: 618px; top: 371px; width: 40px; height: 2px; background: var(--rose-light); }

  /* Welcome */
  .welcome { left: 0; top: 414px; width: 1200px; height: 168px; background: var(--canvas-grey); }
  .welcome-photo {
    left: 287px; top: 442px; width: 236px; height: 114px;
    background: linear-gradient(100deg, #e9707f 0%, #f3a7a5 35%, #8a4b3a 65%, #f2d23c 85%, #d9c7b0 100%);
  }
  .welcome-title { left: 538px; top: 440px; font-size: 10px; color: var(--ink); }
  .welcome-title b { font-weight: 700; }
  .body-copy { font-size: 7.2px; line-height: 13.5px; color: var(--ink); }
  .welcome-copy-1 { left: 538px; top: 471px; width: 380px; }
  .welcome-copy-2 { left: 538px; top: 529px; width: 380px; }

  /* Content panel */
  .content-panel { left: 266px; top: 582px; width: 671px; height: 338px; background: var(--white); border-radius: 0 0 6px 6px; z-index: 2; }
  .col { top: 662px; width: 186px; z-index: 3; }
  .col-products { left: 286px; }
  .col-gallery { left: 510px; }
  .col-testimonial { left: 731px; }
  .col-title { font-size: 10px; color: var(--ink); }
  .col-title b { font-weight: 700; }
  .col-sub { margin-top: 2px; font-size: 7.5px; color: var(--rose); }
  .col-rule { position: relative; margin-top: 6px; height: 1px; background: var(--rule); }
  .col-rule::before { content: ""; position: absolute; left: 0; top: -1px; width: 57px; height: 2px; background: var(--rose-light); }
  .col-arrows { position: absolute; right: 0; top: 2px; display: flex; gap: 3px; }
  .col-arrow { width: 12px; height: 10px; background: var(--rose-pale); display: flex; align-items: center; justify-content: center; }
  .col-copy { margin-top: 12px; }

  .gallery-grid { margin-top: 15px; display: grid; grid-template-columns: 85px 85px; column-gap: 15px; row-gap: 11px; }
  .gallery-tile { position: relative; height: 63px; display: flex; align-items: center; justify-content: center; }
  .tile-1 { background: linear-gradient(135deg, #2f3b4a, #8c6a55 60%, #c9a48c); }
  .tile-2 { background: linear-gradient(135deg, #f3efea, #e2b69b 55%, #c88d74); }
  .tile-3 { background: linear-gradient(135deg, #efe9e4, #c49073 50%, #5a3b2e); }
  .tile-4 { background: linear-gradient(135deg, #f4e2e4, #e7b39d 55%, #d87f95); }
  .tile-badge { width: 22px; height: 22px; border-radius: 50%; background: rgba(185,156,143,0.55); display: flex; align-items: center; justify-content: center; }

  .quote-box { position: relative; margin-top: 14px; height: 83px; background: var(--blush); padding: 10px 12px 0 12px; }
  .quote-box::after { content: ""; position: absolute; left: 88px; bottom: -6px; border-left: 6px solid transparent; border-right: 6px solid transparent; border-top: 6px solid var(--blush); }
  .quote-mark { font-size: 16px; line-height: 10px; color: var(--white); font-weight: 700; }
  .quote-copy { margin-top: 2px; }
  .quote-author { margin-top: 13px; text-align: center; font-size: 8.5px; color: var(--rose); }
  .quote-role { text-align: center; font-size: 7.5px; font-style: italic; color: var(--ink-soft); margin-top: 1px; }

  /* Footer */
  .footer { left: 0; top: 908px; width: 1200px; height: 92px; background: var(--charcoal); }
  .footer-brand { left: 575px; top: 938px; color: #d9c0b5; z-index: 3; }
  .footer-brand .brand-dot { background: #d9c0b5; width: 18px; height: 18px; }
  .footer-brand .brand-name { font-size: 16px; }
  .footer-links { left: 0; top: 975px; width: 1200px; text-align: center; font-size: 6.5px; color: #cccccc; }
  .footer-copy { left: 0; top: 984px; width: 1200px; text-align: center; font-size: 6px; color: #aaaaaa; }
</style>
</head>
<body>
<div class="page">

  <!-- Hero -->
  <div class="abs hero"></div>
  <div class="abs hero-photo" role="img" aria-label="Black and white portrait photograph of a woman in profile touching her neck"></div>

  <div class="abs util-link" style="left:716px;">Lorem ipsum</div>
  <div class="abs util-tab"></div>
  <div class="abs util-link" style="left:795px;">Lorem ipsum</div>
  <div class="abs cart">In Your CART ( 0 )</div>
  <svg class="abs cart-icon" width="15" height="12" viewBox="0 0 15 12" aria-hidden="true">
    <path d="M0.5 1 H3 L5 8 H12.5 L14 3 H4" fill="none" stroke="#777" stroke-width="1.2"/>
    <circle cx="6" cy="10.5" r="1.1" fill="#777"/><circle cx="11.5" cy="10.5" r="1.1" fill="#777"/>
  </svg>

  <div class="abs brand hero-brand"><span class="brand-dot"></span><span class="brand-name">MossVane</span></div>
  <h1 class="abs hero-title" style="font-weight:400;">FLAWLESS BEAUTY</h1>
  <p class="abs hero-lead">Lorem ipsum dolor sit amet, consectetur adipisicing elit</p>

  <div class="abs slide-btn slide-prev"><svg width="12" height="14" viewBox="0 0 12 14"><path d="M9 1 L3 7 L9 13" fill="none" stroke="#fff" stroke-width="1.6"/></svg></div>
  <div class="abs slide-btn slide-next"><svg width="12" height="14" viewBox="0 0 12 14"><path d="M3 1 L9 7 L3 13" fill="none" stroke="#fff" stroke-width="1.6"/></svg></div>

  <div class="abs social" style="left:846px;"></div>
  <div class="abs social" style="left:870px;"></div>
  <div class="abs social" style="left:894px;"></div>
  <div class="abs social social-plus" style="left:918px;"><svg width="11" height="11" viewBox="0 0 11 11"><path d="M5.5 1 V10 M1 5.5 H10" stroke="#fff" stroke-width="2.4"/></svg></div>

  <!-- Navigation -->
  <div class="abs nav-band"></div>
  <div class="abs nav-panel"></div>
  <div class="abs brand nav-brand"><span class="brand-dot"></span><span class="brand-name">MossVane</span></div>
  <nav>
    <span class="abs nav-item" style="left:627px;">Home</span>
    <span class="abs nav-item" style="left:684px;">Our Services</span>
    <span class="abs nav-item" style="left:765px;">Gallery</span>
    <span class="abs nav-item" style="left:828px;">Blogs</span>
    <span class="abs nav-item" style="left:880px;">Contact Us</span>
  </nav>
  <div class="abs nav-active-bar"></div>

  <!-- Welcome -->
  <div class="abs welcome"></div>
  <div class="abs welcome-photo" role="img" aria-label="Spa still life with pink and yellow frangipani flowers and a bowl of water with stones"></div>
  <h2 class="abs welcome-title" style="font-weight:400;">Welcome <b>Website</b></h2>
  <p class="abs body-copy welcome-copy-1">Lorem ipsum dolor sit amet, consectetur adipisicing elit, sed do eiusmod tempor incididunt ut labore et dolore magna aliqua. Ut enim ad minim veniam, quis nostrud exercitation ullamco laboris nisi ut aliquip ex ea commodo consequat. Duis aute irure dolor in reprehenderit in voluptate velit esse cillum dolore eu fugiat nulla pariatur.</p>
  <p class="abs body-copy welcome-copy-2">Lorem ipsum dolor sit amet, consectetur adipisicing elit, sed do eiusmod tempor incididunt ut labore et dolore magna aliqua.</p>

  <!-- Footer band (behind panel) -->
  <div class="abs footer"></div>

  <!-- Content panel -->
  <div class="abs content-panel"></div>

  <section class="abs col col-products">
    <div style="position:relative;">
      <h3 class="col-title" style="font-weight:400;">Our <b>Products</b></h3>
      <div class="col-arrows">
        <span class="col-arrow"><svg width="6" height="6" viewBox="0 0 6 6"><path d="M4.5 0.5 L1.5 3 L4.5 5.5" fill="none" stroke="#fff" stroke-width="1"/></svg></span>
        <span class="col-arrow"><svg width="6" height="6" viewBox="0 0 6 6"><path d="M1.5 0.5 L4.5 3 L1.5 5.5" fill="none" stroke="#fff" stroke-width="1"/></svg></span>
      </div>
      <p class="col-sub">Sub Heading for gallery</p>
      <div class="col-rule"></div>
    </div>
    <p class="body-copy col-copy">Lorem ipsum dolor sit amet, consectetur adipisicing elit, sed do eiusmod tempor incididunt ut labore et dolore magna aliqua.</p>
  </section>

  <section class="abs col col-gallery">
    <div style="position:relative;">
      <h3 class="col-title" style="font-weight:400;">From <b>Gallery</b></h3>
      <div class="col-arrows">
        <span class="col-arrow"><svg width="6" height="6" viewBox="0 0 6 6"><path d="M4.5 0.5 L1.5 3 L4.5 5.5" fill="none" stroke="#fff" stroke-width="1"/></svg></span>
        <span class="col-arrow"><svg width="6" height="6" viewBox="0 0 6 6"><path d="M1.5 0.5 L4.5 3 L1.5 5.5" fill="none" stroke="#fff" stroke-width="1"/></svg></span>
      </div>
      <p class="col-sub">Sub Heading for gallery</p>
      <div class="col-rule"></div>
    </div>
    <div class="gallery-grid">
      <div class="gallery-tile tile-1" role="img" aria-label="Spa photo of a woman with hair up seen from behind"><span class="tile-badge"><svg width="8" height="8" viewBox="0 0 8 8"><path d="M4 0.5 V7.5 M0.5 4 H7.5" stroke="#fff" stroke-width="1.2"/></svg></span></div>
      <div class="gallery-tile tile-2" role="img" aria-label="Spa photo of a facial massage treatment"><span class="tile-badge"><svg width="8" height="8" viewBox="0 0 8 8"><path d="M4 0.5 V7.5 M0.5 4 H7.5" stroke="#fff" stroke-width="1.2"/></svg></span></div>
      <div class="gallery-tile tile-3" role="img" aria-label="Spa photo of a hot stone back massage"><span class="tile-badge"><svg width="8" height="8" viewBox="0 0 8 8"><path d="M4 0.5 V7.5 M0.5 4 H7.5" stroke="#fff" stroke-width="1.2"/></svg></span></div>
      <div class="gallery-tile tile-4" role="img" aria-label="Spa photo of a pedicure with pink petals"><span class="tile-badge"><svg width="8" height="8" viewBox="0 0 8 8"><path d="M4 0.5 V7.5 M0.5 4 H7.5" stroke="#fff" stroke-width="1.2"/></svg></span></div>
    </div>
  </section>

  <section class="abs col col-testimonial">
    <div style="position:relative;">
      <h3 class="col-title">Testimonial</h3>
      <div class="col-arrows">
        <span class="col-arrow"><svg width="6" height="6" viewBox="0 0 6 6"><path d="M4.5 0.5 L1.5 3 L4.5 5.5" fill="none" stroke="#fff" stroke-width="1"/></svg></span>
        <span class="col-arrow"><svg width="6" height="6" viewBox="0 0 6 6"><path d="M1.5 0.5 L4.5 3 L1.5 5.5" fill="none" stroke="#fff" stroke-width="1"/></svg></span>
      </div>
      <p class="col-sub">Sub Heading for testimonial</p>
      <div class="col-rule"></div>
    </div>
    <blockquote class="quote-box">
      <div class="quote-mark">&ldquo;</div>
      <p class="body-copy quote-copy">Lorem ipsum dolor sit amet, consectetur adipisicing elit, sed do eiusmod tempor incididunt ut labore et dolore magna aliqua.</p>
    </blockquote>
    <p class="quote-author">By Admin</p>
    <p class="quote-role">Head of Department</p>
  </section>

  <!-- Footer -->
  <div class="abs brand footer-brand"><span class="brand-dot"></span><span class="brand-name">MossVane</span></div>
  <p class="abs footer-links">Home | Our Service | Gallery | Blog | Contact Us</p>
  <p class="abs footer-copy">Copyright 2014. All Right Reserved.</p>

</div>
</body>
</html>
```